Roof Plumbing Company needs simple, modern business card using the attached logo and below details:

Dean Halloway
Summit Gutters Pty Ltd
ABN: 58 214 937 062
Phone: 0417 286 531
Email: summitgutters@mailbrook.com
Website: summitgutters.com.au

For all of your metal roof plumbing requirements contact Summit Gutters for an obligation free quote - no job too big or to small!

Industry/Entity Type

Business

Contact Information for Business Card

Dean Halloway
Summit Gutters Pty Ltd
ABN 58 214 937 062
0417 286 531
summitgutters@mailbrook.com
summitgutters.com.au

Requirements
Must have
• Bright eye catching design, professional look

```html
<!DOCTYPE html>
<html lang="en">
<head>
<meta charset="UTF-8">
<title>Summit Gutters Pty Ltd — Business Card</title>
<link rel="stylesheet" href="https://fonts.googleapis.com/css2?family=Questrial&display=swap">
<style>
  :root {
    --page-bg: #e9e6e1;
    --card-dark: #3a3b3d;
    --card-mid: #4a4b4e;
    --card-light: #5c5d60;
    --brand-red: #e0202b;
    --brand-red-deep: #b8151f;
    --text-light: #f2f2f2;
    --strip-light: #d9d9d9;
    --rule: rgba(255,255,255,0.55);
  }
  * { margin: 0; padding: 0; box-sizing: border-box; }
  html, body {
    width: 1200px; height: 1022px; overflow: hidden;
    background: var(--page-bg);
    font-family: "Questrial", "Century Gothic", sans-serif;
  }
  .canvas {
    width: 1200px; height: 1022px;
    display: flex; align-items: center; justify-content: center;
  }
  .business-card {
    position: relative;
    width: 1000px; height: 572px;
    background: linear-gradient(120deg, var(--card-mid) 0%, var(--card-light) 45%, var(--card-dark) 100%);
    box-shadow: 0 20px 50px rgba(0,0,0,0.3);
    overflow: hidden;
    color: var(--text-light);
  }
  .bottom-strip {
    position: absolute; left: 0; right: 0; bottom: 0; height: 44px;
    background: linear-gradient(180deg, #eeeeee, var(--strip-light));
  }
  .bottom-strip .accent-red {
    position: absolute; right: 0; top: 0; bottom: 0; width: 330px;
    background: linear-gradient(180deg, var(--brand-red), var(--brand-red-deep));
  }
  .divider-horizontal {
    position: absolute; left: 40px; right: 0; top: 300px;
    height: 1px; background: var(--rule);
  }
  .person-name {
    position: absolute; left: 60px; top: 236px;
    font-size: 44px; letter-spacing: 0.5px; line-height: 1;
  }
  .person-role {
    position: absolute; left: 62px; top: 316px;
    font-size: 22px; line-height: 1; color: var(--brand-red);
  }
  .brand {
    position: absolute; right: 60px; top: 140px;
    display: flex; align-items: center; gap: 18px;
  }
  .brand-dot {
    width: 28px; height: 28px; border-radius: 50%;
    background: var(--brand-red); flex: none;
  }
  .brand-name {
    font-size: 40px; line-height: 1.15; letter-spacing: 3px;
    color: var(--brand-red); text-transform: uppercase;
  }
  .contact-list {
    position: absolute; right: 60px; top: 326px;
    list-style: none; font-size: 21px; line-height: 1;
  }
  .contact-list li {
    display: flex; align-items: center; justify-content: flex-end;
    gap: 12px; margin-bottom: 22px;
  }
  .contact-icon { width: 18px; height: 18px; flex: none; }
  .contact-list .no-icon { padding-right: 30px; }
</style>
</head>
<body>
<main class="canvas">
  <section class="business-card">
    <div class="brand">
      <span class="brand-dot"></span>
      <span class="brand-name">Summit Gutters<br>Pty Ltd</span>
    </div>

    <p class="person-name">Dean Halloway</p>

    <div class="divider-horizontal"></div>

    <p class="person-role">Owner</p>

    <ul class="contact-list">
      <li>
        0417 286 531
        <svg class="contact-icon" viewBox="0 0 24 24" aria-hidden="true"><path fill="#e0202b" d="M6.6 10.8a15.1 15.1 0 0 0 6.6 6.6l2.2-2.2c.3-.3.7-.4 1-.2 1.1.4 2.3.6 3.6.6.6 0 1 .4 1 1V20c0 .6-.4 1-1 1A17 17 0 0 1 3 4c0-.6.4-1 1-1h3.5c.6 0 1 .4 1 1 0 1.3.2 2.5.6 3.6.1.3 0 .7-.2 1z"/></svg>
      </li>
      <li>
        summitgutters@mailbrook.com
        <svg class="contact-icon" viewBox="0 0 24 24" aria-hidden="true"><rect x="2" y="5" width="20" height="14" rx="2" fill="#e0202b"/><path d="M3 6l9 7 9-7" fill="none" stroke="#3a3b3d" stroke-width="1.8"/></svg>
      </li>
      <li>
        www.summitgutters.com.au
        <svg class="contact-icon" viewBox="0 0 24 24" aria-hidden="true"><circle cx="12" cy="12" r="10" fill="#e0202b"/><path d="M2 12h20M12 2c3 3 3 17 0 20M12 2c-3 3-3 17 0 20" fill="none" stroke="#3a3b3d" stroke-width="1.5"/></svg>
      </li>
      <li class="no-icon">ABN: 58 214 937 062</li>
    </ul>

    <div class="bottom-strip"><div class="accent-red"></div></div>
  </section>
</main>
</body>
</html>
```